Munchcart

App Design for a an application on which you can order take aways from restaurants close to you.
(similar app : https://appvault.example/lu/app/grubniq-pizza-burger-sushi/id583017264?l=en&mt=8 )

Logo is a taxi (psd of taxi an font attached)

Attached a draft mockup showing the screens needed.

Screens needed :

1. Splash Screen
2. Select you restaurant screen
3. Select your dish (meat, pizza, pasta....)
4. Select your extras (exta cheese, garlik etc...)
5. Exit screen with total amount and confirmation
6. Subscribe Screen where people have to register the first time.

Target Market(s)

age 14-54

Industry/Entity Type

Restaurant

Requirements
Must have
• Wood elements

```html
<!DOCTYPE html>
<html lang="en">
<head>
<meta charset="utf-8">
<title>Munchcart – App Screens</title>
<link rel="stylesheet" href="https://fonts.googleapis.com/css2?family=Arimo:wght@400;700&family=PT+Sans:wght@400;700&display=swap">
<style>
  :root {
    --page-bg: #ececf0;
    --screen-top: #2e2e2e;
    --screen-bottom: #1e1e1e;
    --wood-dark: #7a3812;
    --wood-mid: #b5642c;
    --wood-light: #d38a4c;
    --wood-edge: #5a2608;
    --wood-ink: #4a1e06;
    --taxi-yellow: #f6b51e;
    --card-bg: #f1eee8;
    --card-text: #555;
    --brand-red: #b31d1d;
    --star: #f2c200;
    --star-off: #d8d8d8;
    --white: #ffffff;
    --label-shadow: rgba(0,0,0,.8);
  }
  * { box-sizing: border-box; margin: 0; padding: 0; }
  html, body { width: 1200px; height: 899px; overflow: hidden; }
  body { background: var(--page-bg); font-family: "Arimo", Arial, sans-serif; position: relative; }

  .screen {
    position: absolute; top: 180px; width: 304px; height: 540px; overflow: hidden;
    background: linear-gradient(var(--screen-top), var(--screen-bottom));
  }
  .screen--home { left: 62px; }
  .screen--splash { left: 452px; background: radial-gradient(ellipse at 50% 45%, #3a3a3a, #1c1c1c 70%); }
  .screen--list { left: 841px; }

  .status-bar {
    height: 20px; background: #000; color: var(--white); font-size: 12px; font-weight: 700;
    display: flex; align-items: center; justify-content: center; position: relative;
  }
  .status-bar .signal { position: absolute; left: 6px; top: 6px; display: flex; gap: 1px; align-items: flex-end; }
  .status-bar .signal i { display: block; width: 2px; background: var(--white); }
  .status-bar .battery { position: absolute; right: 8px; top: 6px; width: 18px; height: 8px; border: 1px solid var(--white); padding: 1px; }
  .status-bar .battery::before { content: ""; display: block; height: 100%; background: var(--white); }

  /* Home screen */
  .app-icon { position: absolute; width: 55px; text-align: center; }
  .app-icon .tile { width: 55px; height: 55px; border-radius: 11px; box-shadow: 0 2px 3px rgba(0,0,0,.6); }
  .app-icon .label { display: block; margin-top: 6px; color: var(--white); font-size: 11px; font-weight: 700; text-shadow: 0 1px 2px var(--label-shadow); white-space: nowrap; margin-left: -10px; margin-right: -10px; }
  .tile--munchcart { background: linear-gradient(var(--wood-light), var(--wood-dark)); display: flex; align-items: center; justify-content: center; }
  .tile--munchcart span { color: var(--taxi-yellow); font-weight: 700; font-size: 9px; }
  .page-dots { position: absolute; top: 447px; left: 0; right: 0; display: flex; justify-content: center; gap: 9px; }
  .page-dots i { width: 6px; height: 6px; border-radius: 50%; background: #888; }
  .page-dots i.active { background: var(--white); }
  .page-dots i.search { background: none; border: 1.5px solid #888; }
  .dock { position: absolute; left: 0; right: 0; top: 496px; height: 44px; background: linear-gradient(rgba(255,255,255,.25), rgba(255,255,255,.08)); border-top: 1px solid rgba(255,255,255,.4); }

  /* Wood bars */
  .wood-bar {
    position: absolute; left: 0; right: 0; height: 35px;
    background: linear-gradient(var(--wood-light), var(--wood-mid) 55%, var(--wood-dark));
    border-bottom: 1px solid var(--wood-edge);
  }
  .wood-bar--top { top: 20px; }
  .app-title { text-align: center; line-height: 35px; font-size: 13px; font-weight: 700; color: #7a3a17; letter-spacing: .5px; }

  /* Splash */
  .splash-logo { position: absolute; left: 52px; top: 222px; width: 200px; display: flex; align-items: center; justify-content: center; gap: 8px; }
  .splash-logo .mark { width: 20px; height: 20px; border-radius: 50%; background: var(--taxi-yellow); }
  .splash-logo .name { color: var(--taxi-yellow); font-size: 24px; font-weight: 700; }
  .progress { position: absolute; left: 44px; top: 306px; width: 217px; height: 18px; border-radius: 9px; background: #222; box-shadow: inset 0 1px 3px #000; }
  .progress .fill { width: 61%; height: 100%; border-radius: 9px; background: linear-gradient(var(--wood-light), var(--wood-dark)); font-size: 9px; color: #f3d9c0; line-height: 18px; text-align: right; padding-right: 20px; }

  /* Restaurant list */
  .btn-back { position: absolute; left: 16px; top: 8px; height: 20px; padding: 0 8px 0 12px; background: #f1efed; border-radius: 4px; font-size: 9px; line-height: 20px; color: #333; clip-path: polygon(8px 0, 100% 0, 100% 100%, 8px 100%, 0 50%); }
  .search-field { position: absolute; left: 96px; top: 7px; width: 114px; height: 21px; border-radius: 11px; background: #f1efed; border: 2px solid #d8d2cb; font-size: 8px; line-height: 17px; padding-left: 22px; color: #444; }
  .search-field svg { position: absolute; left: 7px; top: 4px; }
  .btn-fav { position: absolute; right: 16px; top: 7px; width: 42px; height: 21px; background: #f1efed; border-radius: 3px; text-align: center; line-height: 21px; font-size: 12px; color: #555; }
  .section-head { position: absolute; left: 95px; top: 71px; color: var(--white); font-size: 10px; font-weight: 700; letter-spacing: .3px; }
  .section-logo { position: absolute; left: 226px; top: 69px; display: flex; align-items: center; gap: 3px; }
  .section-logo .mark { width: 9px; height: 9px; border-radius: 50%; background: var(--taxi-yellow); }
  .section-logo .name { color: var(--taxi-yellow); font-size: 10px; font-weight: 700; }
  .scroll-track { position: absolute; left: 295px; top: 94px; width: 4px; height: 300px; background: #ddd; border-radius: 2px; }
  .scroll-thumb { position: absolute; left: 293px; top: 100px; width: 8px; height: 40px; border-radius: 3px; background: var(--wood-mid); }

  .restaurant { position: absolute; left: 19px; width: 266px; height: 55px; }
  .restaurant .badge { position: absolute; left: 0; top: 0; width: 55px; height: 55px; border-radius: 6px; padding: 5px; background: linear-gradient(var(--wood-light), var(--wood-dark)); box-shadow: 0 1px 3px #000; }
  .restaurant .badge span { display: flex; align-items: center; justify-content: center; width: 100%; height: 100%; background: var(--white); border-radius: 3px; font-size: 8px; font-weight: 700; text-align: center; color: var(--brand-red); line-height: 1.1; }
  .restaurant .info { position: absolute; left: 70px; top: 0; width: 196px; height: 55px; background: var(--card-bg); border-radius: 3px; padding: 4px 5px; font-family: "PT Sans", Arial, sans-serif; font-weight: 700; font-size: 7.5px; line-height: 1.3; color: var(--card-text); }
  .stars { position: absolute; right: 5px; bottom: 3px; font-size: 9px; letter-spacing: -.5px; color: var(--star); }
  .stars b { color: var(--star-off); font-weight: 400; }

  .wood-bar--bottom { top: 496px; height: 44px; border-top: 1px solid var(--wood-edge); display: flex; justify-content: space-around; align-items: center; }
  .tab { width: 42px; display: flex; justify-content: center; opacity: .85; }
  .tab + .tab { border-left: 1px solid rgba(0,0,0,.25); }
</style>
</head>
<body>

<section class="screen screen--home" aria-label="Home screen">
  <div class="status-bar"><span class="signal"><i style="height:3px"></i><i style="height:4px"></i><i style="height:5px"></i><i style="height:6px"></i><i style="height:7px"></i></span>9:40 AM<span class="battery"></span></div>

  <div class="app-icon" style="left:15px;top:33px"><div class="tile" role="img" aria-label="Messages app icon" style="background:linear-gradient(#7ee067,#23a322)"></div><span class="label">Messages</span></div>
  <div class="app-icon" style="left:87px;top:33px"><div class="tile" role="img" aria-label="Calendar app icon" style="background:linear-gradient(#f08a2a 0 22%,#fff 22%)"></div><span class="label">Calendar</span></div>
  <div class="app-icon" style="left:160px;top:33px"><div class="tile" role="img" aria-label="Photos app icon" style="background:linear-gradient(#dfe9f3,#8fb1cf)"></div><span class="label">Photos</span></div>
  <div class="app-icon" style="left:232px;top:33px"><div class="tile" role="img" aria-label="Camera app icon" style="background:linear-gradient(#d0d0d0,#888)"></div><span class="label">Camera</span></div>

  <div class="app-icon" style="left:15px;top:117px"><div class="tile" role="img" aria-label="Videos app icon" style="background:linear-gradient(#7fb3ea,#1d5ea8)"></div><span class="label">Videos</span></div>
  <div class="app-icon" style="left:87px;top:117px"><div class="tile" role="img" aria-label="Maps app icon" style="background:linear-gradient(135deg,#f3e6b8,#b9d59a)"></div><span class="label">Maps</span></div>
  <div class="app-icon" style="left:160px;top:117px"><div class="tile" role="img" aria-label="Weather app icon" style="background:linear-gradient(#6fb7f0,#2a78c8)"></div><span class="label">Weather</span></div>
  <div class="app-icon" style="left:232px;top:117px"><div class="tile" role="img" aria-label="Memos app icon" style="background:linear-gradient(#777,#333)"></div><span class="label">Memos</span></div>

  <div class="app-icon" style="left:15px;top:200px"><div class="tile" role="img" aria-label="To Do app icon" style="background:linear-gradient(#7a4a2a 0 22%,#fbf1a6 22%)"></div><span class="label">To Do</span></div>
  <div class="app-icon" style="left:87px;top:200px"><div class="tile" role="img" aria-label="Clock app icon" style="background:linear-gradient(#ddd,#777)"></div><span class="label">Clock</span></div>
  <div class="app-icon" style="left:160px;top:200px"><div class="tile" role="img" aria-label="People app icon" style="background:linear-gradient(#c98c46,#8c5726)"></div><span class="label">People</span></div>
  <div class="app-icon" style="left:232px;top:200px"><div class="tile" role="img" aria-label="Newsfeed app icon" style="background:linear-gradient(#b76ae0,#6a2ba0)"></div><span class="label">Newsfeed</span></div>

  <div class="app-icon" style="left:15px;top:284px"><div class="tile" role="img" aria-label="Settings app icon" style="background:linear-gradient(#bbb,#666)"></div><span class="label">Settings</span></div>
  <div class="app-icon" style="left:87px;top:284px"><div class="tile tile--munchcart"><span>Munchcart</span></div><span class="label">Munchcart</span></div>

  <div class="page-dots"><i class="search"></i><i class="active"></i><i></i></div>
  <div class="dock"></div>

  <div class="app-icon" style="left:15px;top:466px"><div class="tile" role="img" aria-label="Phone app icon" style="background:linear-gradient(#7ee067,#23a322)"></div><span class="label">Phone</span></div>
  <div class="app-icon" style="left:87px;top:466px"><div class="tile" role="img" aria-label="Mail app icon" style="background:linear-gradient(#8cc4f4,#2a6fc4)"></div><span class="label">Mail</span></div>
  <div class="app-icon" style="left:160px;top:466px"><div class="tile" role="img" aria-label="Internet app icon" style="background:linear-gradient(#a8d4f4,#3f84c8)"></div><span class="label">Internet</span></div>
  <div class="app-icon" style="left:232px;top:466px"><div class="tile tile--munchcart"><span>Munchcart</span></div><span class="label">Munchcart</span></div>
</section>

<section class="screen screen--splash" aria-label="Splash screen">
  <div class="status-bar"><span class="signal"><i style="height:3px"></i><i style="height:4px"></i><i style="height:5px"></i><i style="height:6px"></i><i style="height:7px"></i></span>9:40 AM<span class="battery"></span></div>
  <header class="wood-bar wood-bar--top"><h1 class="app-title">MUNCHCART</h1></header>
  <div class="splash-logo"><span class="mark"></span><span class="name">Munchcart</span></div>
  <div class="progress"><div class="fill">58%</div></div>
</section>

<section class="screen screen--list" aria-label="Select restaurant screen">
  <div class="status-bar"><span class="signal"><i style="height:3px"></i><i style="height:4px"></i><i style="height:5px"></i><i style="height:6px"></i><i style="height:7px"></i></span>9:40 AM<span class="battery"></span></div>
  <header class="wood-bar wood-bar--top">
    <span class="btn-back">Back</span>
    <span class="search-field"><svg width="9" height="9" viewBox="0 0 10 10"><circle cx="4" cy="4" r="3" fill="none" stroke="#555" stroke-width="1.5"/><line x1="6.3" y1="6.3" x2="9.5" y2="9.5" stroke="#555" stroke-width="1.5"/></svg>FAST FOOD</span>
    <span class="btn-fav">★</span>
  </header>

  <h2 class="section-head">SELECT RESTAURANT</h2>
  <div class="section-logo"><span class="mark"></span><span class="name">Munchcart</span></div>
  <div class="scroll-track"></div><div class="scroll-thumb"></div>

  <article class="restaurant" style="top:100px">
    <div class="badge"><span>Grillhaus</span></div>
    <p class="info">Maecenas pharetra neque ac magna bibendum in aliquet elit mattis. Sed nunc tortore.<span class="stars">★★★★<b>★</b></span></p>
  </article>
  <article class="restaurant" style="top:165px">
    <div class="badge"><span>Pieworks</span></div>
    <p class="info">Maecenas sagittis malesuada lorem, sit amet iaculis est dignissim id. Pellentesque habitant morbi tristique senectus.<span class="stars">★★★<b>★★</b></span></p>
  </article>
  <article class="restaurant" style="top:230px">
    <div class="badge"><span>Via Nonna</span></div>
    <p class="info">Vivamus quis tortor ante, vel vehicula leo. Nunc faucibus, sem sed tristique venenatis.<span class="stars">★★<b>★★★</b></span></p>
  </article>
  <article class="restaurant" style="top:295px">
    <div class="badge"><span>Fork &amp; Fire</span></div>
    <p class="info">Praesent varius nibh at sapien sodales pharetra. Sed id arcu nunc. Donec eros velit, scelerisque nec egestas vitae, placerat eget nisl.<span class="stars">★<b>★★★★</b></span></p>
  </article>
  <article class="restaurant" style="top:360px">
    <div class="badge"><span>Brewline</span></div>
    <p class="info">Pellentesque vestibulum semper dui, et sagittis mi condimentum et. Phasellus porttitor viverra dapibus. Ut commodo facilisis consequat. Maecenas vel gravida elit<span class="stars">★★★<b>★★</b></span></p>
  </article>
  <article class="restaurant" style="top:425px">
    <div class="badge"><span>Redpepper</span></div>
    <p class="info">Pellentesque vestibulum semper dui, et sagittis mi condimentum et. Phasellus porttitor viverra dapibus.<span class="stars">★★★★★</span></p>
  </article>

  <nav class="wood-bar wood-bar--bottom" aria-label="Tab bar">
    <span class="tab"><svg width="26" height="20" viewBox="0 0 26 20"><path d="M2 7c3-5 19-5 22 0l-1 3-5-1-1-3H9L8 9 3 10z" fill="var(--wood-ink)"/><rect x="7" y="11" width="12" height="8" rx="2" fill="var(--wood-ink)"/></svg></span>
    <span class="tab"><svg width="22" height="22" viewBox="0 0 22 22"><path d="M4 3v6c0 2 2 3 3 3v8h2v-8c1 0 3-1 3-3V3h-1.5v5H9.5V3H8v5H6.5V3zM17 2c-3 2-3 8-1 10v8h2V2z" fill="var(--wood-ink)"/></svg></span>
    <span class="tab"><svg width="20" height="20" viewBox="0 0 20 20"><circle cx="8" cy="8" r="6" fill="none" stroke="var(--wood-ink)" stroke-width="2.5"/><line x1="12.5" y1="12.5" x2="18" y2="18" stroke="var(--wood-ink)" stroke-width="3"/></svg></span>
    <span class="tab"><svg width="24" height="20" viewBox="0 0 24 20"><path d="M2 11l6 6L22 3" fill="none" stroke="var(--wood-ink)" stroke-width="3.5"/></svg></span>
    <span class="tab"><svg width="28" height="20" viewBox="0 0 28 20"><rect x="1" y="1" width="26" height="18" rx="2" fill="none" stroke="var(--wood-ink)" stroke-width="2"/><circle cx="9" cy="8" r="3" fill="var(--wood-ink)"/><path d="M4 16c0-4 10-4 10 0z" fill="var(--wood-ink)"/><rect x="16" y="6" width="8" height="2" fill="var(--wood-ink)"/><rect x="16" y="10" width="8" height="2" fill="var(--wood-ink)"/><rect x="16" y="14" width="8" height="2" fill="var(--wood-ink)"/></svg></span>
  </nav>
</section>

</body>
</html>
```